TL Estates
Desmond Parkes
TL Estates - Real Estate
Creative Brief
Corporate
Owner/ Realtor
Suite # 17 Ashbury Business Centre, 28 Calder Rd. Kingston 5
dp@desmondparkes-example.com
www.desmondparkes-example.com
Business card , Letter head and envelopes to compliment LOGO i DO NOT WANT MY PICTURE TO APPEAR IN A BOX...I WOULD WANT IT TO BE FLOATING ON THE BUSINESS CARD I would like for the designers to colour my shirt RED

```html
<!DOCTYPE html>
<html lang="en">
<head>
<meta charset="utf-8">
<title>TL Estates — Stationery Set</title>
<link href="https://fonts.googleapis.com/css2?family=Open+Sans:wght@400;600;700&display=swap" rel="stylesheet">
<style>
  :root {
    --bg: #2a2a2a;
    --paper: #ffffff;
    --red: #c8161d;
    --red-dark: #8e0f14;
    --grey: #8a8a8a;
    --grey-light: #d9d9d9;
    --ink: #333333;
    --faint: #f1e6e3;
  }
  * { margin: 0; padding: 0; box-sizing: border-box; }
  html, body { width: 1200px; height: 574px; overflow: hidden; }
  body { background: var(--bg); font-family: "Open Sans", sans-serif; color: var(--ink); position: relative; }

  .sheet { position: absolute; background: var(--paper); overflow: hidden; }
  .letterhead { left: 36px; top: 96px; width: 408px; height: 420px; }
  .fax-sheet { left: 480px; top: 96px; width: 408px; height: 420px; }

  .brand { position: absolute; left: 0; right: 0; text-align: center; }
  .brand-mark { display: block; width: 26px; height: 26px; background: var(--red); margin: 0 auto 4px; }
  .brand-name { display: block; color: var(--red); font-weight: 700; font-size: 10px; letter-spacing: 1px; text-transform: uppercase; white-space: nowrap; }
  .brand-tag { display: block; color: var(--grey); font-size: 5px; letter-spacing: 1px; margin-top: 1px; }
  .letterhead .brand, .fax-sheet .brand { top: 22px; }

  .backdrop-name { position: absolute; left: 0; right: 0; top: 180px; text-align: center; color: var(--faint); font-size: 34px; font-weight: 700; white-space: nowrap; }

  .swoosh { position: absolute; left: 0; bottom: 0; width: 100%; height: 60px; }
  .footer-url { position: absolute; left: 12px; bottom: 9px; color: #fff; font-size: 5.5px; }
  .footer-info { position: absolute; bottom: 10px; display: flex; gap: 18px; font-size: 4.5px; color: var(--grey); line-height: 1.5; }
  .letterhead .footer-info, .fax-sheet .footer-info { right: 26px; }

  .fax-title { position: absolute; left: 40px; top: 86px; font-size: 18px; font-weight: 600; letter-spacing: 1px; }
  .fax-fields { position: absolute; left: 40px; right: 40px; top: 120px; display: grid; grid-template-columns: 1fr 1fr; column-gap: 22px; row-gap: 12px; }
  .fax-field { font-size: 5px; border-bottom: 1px solid var(--grey-light); padding-bottom: 2px; }
  .fax-options { position: absolute; left: 40px; right: 40px; top: 200px; display: flex; justify-content: space-between; font-size: 5px; }
  .fax-options span::before { content: ""; display: inline-block; width: 5px; height: 5px; border: 1px solid var(--grey); margin-right: 3px; vertical-align: -1px; }

  .envelope { position: absolute; left: 924px; width: 264px; background: var(--paper); overflow: hidden; }
  .envelope-back { top: 48px; height: 144px; }
  .envelope-front { top: 197px; height: 151px; }
  .envelope-back .brand { top: 8px; }
  .envelope-back .brand-mark { width: 16px; height: 16px; background: #fff; }
  .envelope-back .brand-name { color: #fff; font-size: 6px; }
  .envelope-front .brand { left: 10px; right: auto; top: 12px; text-align: left; }
  .envelope-front .brand-mark { width: 14px; height: 14px; margin: 0 0 2px; }
  .envelope-front .brand-name { font-size: 6px; }
  .envelope-front .return { position: absolute; left: 10px; top: 46px; font-size: 4px; color: var(--grey); line-height: 1.5; }
  .envelope-front .backdrop-name { left: auto; right: 14px; top: 98px; font-size: 11px; }
  .envelope-front .site { position: absolute; left: 10px; bottom: 10px; font-size: 4.5px; color: var(--red); }

  .card { position: absolute; width: 120px; height: 72px; background: var(--paper); overflow: hidden; }
  .card-a { left: 924px; top: 372px; }
  .card-b { left: 1056px; top: 372px; }
  .card-c { left: 924px; top: 456px; }
  .card-d { left: 1056px; top: 456px; background: linear-gradient(160deg, var(--red), var(--red-dark)); }
  .portrait { position: absolute; width: 26px; height: 40px; background: linear-gradient(180deg, #6b4a3a 0 30%, var(--red) 30%); border-radius: 10px 10px 0 0; }
  .card-a .portrait { left: 8px; top: 20px; }
  .card-c .portrait { right: 10px; top: 22px; }
  .card .brand { top: 6px; }
  .card .brand-mark { width: 12px; height: 12px; margin-bottom: 2px; }
  .card .brand-name { font-size: 5px; }
  .card-a .brand { left: 40px; right: 4px; }
  .card-c .brand { left: 4px; right: 40px; }
  .card-b .brand { top: 20px; }
  .card-d .brand { top: 22px; }
  .card-d .brand-mark { background: #fff; }
  .card-d .brand-name { color: #fff; }
  .card-person { position: absolute; font-size: 4px; line-height: 1.5; }
  .card-person b { display: block; font-size: 5px; color: var(--red); }
  .card-a .card-person { left: 42px; top: 34px; }
  .card-c .card-person { left: 8px; top: 34px; }
  .card-band { position: absolute; left: 0; bottom: 0; width: 100%; height: 14px; }
  .card-band-text { position: absolute; left: 6px; bottom: 3px; font-size: 3.5px; color: #fff; }
</style>
</head>
<body>

<section class="sheet letterhead">
  <div class="brand">
    <span class="brand-mark"></span>
    <span class="brand-name">TL Estates</span>
    <span class="brand-tag">REAL ESTATE SERVICES</span>
  </div>
  <div class="backdrop-name">TL Estates</div>
  <svg class="swoosh" viewBox="0 0 408 60" preserveAspectRatio="none">
    <path d="M0 30 C120 48 260 52 408 40 L408 60 L0 60 Z" fill="#e5e5e5"/>
    <path d="M0 36 C90 46 170 50 240 60 L0 60 Z" fill="var(--red)"/>
  </svg>
  <span class="footer-url">www.desmondparkes-example.com</span>
  <div class="footer-info">
    <div>Suite # 17<br>Ashbury Business Centre<br>28 Calder Rd. Kingston 5</div>
    <div>Tel: 876-555-0142<br>Fax: 876-555-0143<br>dp@desmondparkes-example.com</div>
  </div>
</section>

<section class="sheet fax-sheet">
  <div class="brand">
    <span class="brand-mark"></span>
    <span class="brand-name">TL Estates</span>
    <span class="brand-tag">REAL ESTATE SERVICES</span>
  </div>
  <h1 class="fax-title">FAX</h1>
  <div class="fax-fields">
    <div class="fax-field">To:</div><div class="fax-field">From:</div>
    <div class="fax-field">Fax:</div><div class="fax-field">Pages:</div>
    <div class="fax-field">Phone:</div><div class="fax-field">Date:</div>
    <div class="fax-field">Re:</div><div class="fax-field">CC:</div>
  </div>
  <div class="fax-options">
    <span>Urgent</span><span>For Review</span><span>Please Comment</span><span>Please Reply</span><span>Please Recycle</span>
  </div>
  <svg class="swoosh" viewBox="0 0 408 60" preserveAspectRatio="none">
    <path d="M0 30 C120 48 260 52 408 40 L408 60 L0 60 Z" fill="#e5e5e5"/>
    <path d="M0 36 C90 46 170 50 240 60 L0 60 Z" fill="var(--red)"/>
  </svg>
  <span class="footer-url">www.desmondparkes-example.com</span>
  <div class="footer-info">
    <div>Suite # 17<br>Ashbury Business Centre<br>28 Calder Rd. Kingston 5</div>
    <div>Tel: 876-555-0142<br>Fax: 876-555-0143<br>dp@desmondparkes-example.com</div>
  </div>
</section>

<section class="envelope envelope-back">
  <svg width="264" height="144" viewBox="0 0 264 144" style="position:absolute;left:0;top:0">
    <path d="M0 0 H264 V30 L132 70 L0 30 Z" fill="var(--red)"/>
    <path d="M0 30 L132 70 L264 30" fill="none" stroke="var(--red-dark)" stroke-width="1"/>
    <path d="M0 144 L110 86 M264 144 L154 86" stroke="var(--grey-light)" stroke-width="1"/>
  </svg>
  <div class="brand">
    <span class="brand-mark"></span>
    <span class="brand-name">TL Estates</span>
  </div>
</section>

<section class="envelope envelope-front">
  <div class="brand">
    <span class="brand-mark"></span>
    <span class="brand-name">TL Estates</span>
  </div>
  <div class="return">Suite # 17 Ashbury Business Centre<br>28 Calder Rd. Kingston 5</div>
  <div class="backdrop-name">TL Estates</div>
  <span class="site">www.desmondparkes-example.com</span>
</section>

<section class="card card-a">
  <div class="portrait" role="img" aria-label="Portrait of Desmond Parkes in a red shirt"></div>
  <div class="brand"><span class="brand-mark"></span><span class="brand-name">TL Estates</span></div>
  <div class="card-person"><b>Desmond Parkes</b>Owner / Realtor<br>876-555-0142</div>
  <svg class="card-band" viewBox="0 0 120 14" preserveAspectRatio="none"><path d="M0 4 C40 10 80 12 120 2 V14 H0 Z" fill="var(--red)"/></svg>
  <span class="card-band-text">dp@desmondparkes-example.com</span>
</section>

<section class="card card-b">
  <div class="brand"><span class="brand-mark"></span><span class="brand-name">TL Estates</span></div>
  <svg class="card-band" viewBox="0 0 120 14" preserveAspectRatio="none"><path d="M0 8 C40 12 80 12 120 6 V14 H0 Z" fill="var(--red)"/></svg>
</section>

<section class="card card-c">
  <div class="portrait" role="img" aria-label="Portrait of Desmond Parkes in a red shirt"></div>
  <div class="brand"><span class="brand-mark"></span><span class="brand-name">TL Estates</span></div>
  <div class="card-person"><b>Desmond Parkes</b>Owner / Realtor<br>876-555-0142</div>
  <svg class="card-band" viewBox="0 0 120 14" preserveAspectRatio="none"><path d="M0 2 C40 12 80 10 120 4 V14 H0 Z" fill="var(--red)"/></svg>
  <span class="card-band-text">www.desmondparkes-example.com</span>
</section>

<section class="card card-d">
  <div class="brand"><span class="brand-mark"></span><span class="brand-name">TL Estates</span></div>
</section>

</body>
</html>
```